Brivonex Letter head

Brivonex is a young and energetic software development consultancy. We spend our time working with clients to turn what ever is in their heads in to software.
We are trying to create an image of a high class software boutique who build class leading bespoke solutions.
We need a sharp letter head that looks great on high quality media.
We like bold colours and distinctive design. So show us what you can do.
Industry/Entity Type
Software
Requirements
Must have
- Our company is based in the UK and are requried to have on the paper somewhere the following information:
* Registered company name: Brivonex Ltd
* Registered company number
* VAT registration number
In addition we also want the following:
* An email address
* Telephone number
* Website address
An example of what some pages have in their footer is something like the following:
Brivonex Ltd is registered in England and Wales. Reg. no: 5316240
Registered office: 41 Pellowmore Road, Hartcombe Middlesex, HC47QD. Tel: 07812365091
You do not have to use this sentance but please make sure your design incorporates accommodates the requirements for UK based companies

```html
<!DOCTYPE html>
<html lang="en">
<head>
<meta charset="utf-8">
<title>Brivonex Letterhead</title>
<link rel="stylesheet" href="https://fonts.googleapis.com/css2?family=Didact+Gothic&display=swap">
<style>
  :root {
    --backdrop: #abacb4;
    --paper: #f1f2f5;
    --brand-red: #a4202a;
    --ink-grey: #7d7f86;
    --ink-dark: #55575d;
    --on-red: #ffffff;
    --faint-mark: rgba(120, 124, 135, 0.07);
  }
  html, body {
    margin: 0;
    padding: 0;
    width: 1200px;
    height: 982px;
    overflow: hidden;
    background: var(--backdrop);
    font-family: "Didact Gothic", sans-serif;
  }
  .letterhead {
    position: absolute;
    left: 268px;
    top: 21px;
    width: 664px;
    height: 940px;
    background: var(--paper);
    overflow: hidden;
  }
  .brand-band {
    position: absolute;
    left: 30px;
    top: 0;
    width: 272px;
    height: 60px;
    background: var(--brand-red);
    border-bottom-right-radius: 9px;
    display: flex;
    align-items: center;
    padding-left: 22px;
    box-sizing: border-box;
  }
  .brand-name {
    color: var(--on-red);
    font-size: 36px;
    letter-spacing: 1px;
    text-transform: uppercase;
    line-height: 1;
  }
  .web-address {
    position: absolute;
    left: 34px;
    top: 74px;
    font-size: 13px;
    letter-spacing: 6.5px;
    color: var(--ink-grey);
  }
  .rule {
    position: absolute;
    background: var(--brand-red);
  }
  .rule-vertical {
    left: 318px;
    top: 0;
    width: 1px;
    height: 46px;
  }
  .rule-horizontal {
    left: 302px;
    top: 46px;
    width: 362px;
    height: 1px;
  }
  .company-details {
    position: absolute;
    right: 22px;
    top: 62px;
    text-align: right;
    font-size: 8.5px;
    line-height: 13px;
    color: var(--ink-dark);
    margin: 0;
  }
  .company-details .label {
    color: var(--brand-red);
  }
  .background-name {
    position: absolute;
    right: 40px;
    bottom: 230px;
    font-size: 110px;
    color: var(--faint-mark);
    text-transform: uppercase;
    line-height: 1;
  }
</style>
</head>
<body>
  <main class="letterhead">
    <header>
      <div class="brand-band">
        <span class="brand-name">Brivonex</span>
      </div>
      <div class="web-address">www.brivonex.com</div>
      <div class="rule rule-vertical"></div>
      <div class="rule rule-horizontal"></div>
      <address class="company-details">
        41 Pellowmore Road, Hartcombe Middlesex, HC47QD<br>
        <span class="label">T:</span> 07812365091 &nbsp;<span class="label">E:</span> info@brivonex.com<br>
        Brivonex Ltd is registered in England and Wales<br>
        Reg. No: 5316240 · VAT: GB999 9999 73
      </address>
    </header>
    <div class="background-name" aria-hidden="true">Brivonex</div>
  </main>
</body>
</html>
```